Business card for Chiropractic clinics needs reworked / redesigned

The business card in attachment was designed 10 years ago. It is in need of an update.
We have 2 clinics:
HALSPUNT VORDA & HALSPUNT MIRBE
Only one address needs to be on the card for doctors that only work in one clinic and two addresses need to be on the card for the doctors that work in both clinics.

Target Market(s)

patients/referrers

Industry/Entity Type

Medical

Contact Information for Business Card

Logo (in full or zoomed-in)
Clinic Name
Doctor name and title
clinic address, website, tel, email

Font styles to use
Sans Serif

Colors

Designer to choose colors to be used in the design.

Requirements
Must have
• Good contrast/readability
• We like modern minimalistic designs
• The Bcard needs to project our very high standard of proficiency/professionalism
Should not have
• Not curly
• Not to much colours

```html
<!DOCTYPE html>
<html lang="en">
<head>
<meta charset="utf-8">
<title>Halspunt Mirbe – Business Card</title>
<link href="https://fonts.googleapis.com/css2?family=Oswald:wght@600&family=Work+Sans:wght@400;500&display=swap" rel="stylesheet">
<style>
  :root {
    --backdrop: #1c1c1e;
    --card: #121213;
    --card-edge: #1f1f21;
    --silver: #d6d6d8;
    --silver-dim: #9a9a9e;
    --name-tone: #b4b4b8;
    --muted: #85858a;
    --rule: #4a4a4d;
  }
  * { margin: 0; padding: 0; box-sizing: border-box; }
  html, body {
    width: 1200px; height: 900px; overflow: hidden;
    background: var(--backdrop);
  }
  .canvas {
    position: relative; width: 1200px; height: 900px;
    display: flex; flex-direction: column; align-items: center; justify-content: center; gap: 50px;
  }
  .card {
    position: relative; width: 600px; height: 350px;
    background: linear-gradient(135deg, var(--card) 0%, var(--card-edge) 100%);
    box-shadow: 0 14px 30px rgba(0,0,0,0.45);
  }
  /* front */
  .brand-mark {
    position: absolute; left: 0; right: 0; top: 158px;
    text-align: center; padding-left: 60px;
    font-family: 'Work Sans', sans-serif; font-weight: 500;
    font-size: 22px; letter-spacing: 4px; color: var(--silver);
  }
  /* back */
  .identity {
    position: absolute; right: 310px; top: 140px; text-align: right;
  }
  .doctor-name {
    font-family: 'Oswald', sans-serif; font-weight: 600;
    font-size: 30px; line-height: 1; letter-spacing: 0.5px;
    color: var(--name-tone); text-transform: uppercase;
  }
  .doctor-title {
    font-family: 'Work Sans', sans-serif; font-size: 15px;
    color: var(--muted); margin-top: 2px; letter-spacing: 0.5px;
  }
  .divider {
    position: absolute; left: 302px; top: 150px; width: 1px; height: 66px;
    background: var(--rule);
  }
  .contacts {
    position: absolute; left: 318px; top: 148px; list-style: none;
    font-family: 'Work Sans', sans-serif; font-size: 15px;
    color: var(--silver); letter-spacing: 0.6px;
  }
  .contacts li { display: flex; align-items: center; gap: 9px; height: 23px; }
  .contacts svg { width: 11px; height: 11px; flex: none; }
  .clinic {
    position: absolute; left: 0; right: 0; top: 270px; text-align: center;
    font-family: 'Work Sans', sans-serif; color: var(--silver-dim);
    letter-spacing: 1px;
  }
  .clinic-name { font-size: 16px; font-weight: 500; }
  .clinic-address { font-size: 16px; margin-top: 2px; }
</style>
</head>
<body>
<main class="canvas">
  <section class="card card-front" aria-label="Card front">
    <div class="brand-mark">HALSPUNT MIRBE</div>
  </section>

  <section class="card card-back" aria-label="Card back">
    <div class="identity">
      <div class="doctor-name">Lander Verhoeven</div>
      <div class="doctor-title">chiropractor</div>
    </div>
    <div class="divider"></div>
    <ul class="contacts">
      <li>
        <svg viewBox="0 0 12 12" aria-hidden="true"><path d="M3 1 L4.6 3.6 L3.6 4.6 Q4.6 7 7.4 8.4 L8.4 7.4 L11 9 L10 11 Q4 11 1 2 Z" fill="var(--silver)"/></svg>
        09 214 68 40
      </li>
      <li>
        <svg viewBox="0 0 12 12" aria-hidden="true"><rect x="0.8" y="2.3" width="10.4" height="7.4" fill="none" stroke="var(--silver)" stroke-width="1.2"/><path d="M1 2.6 L6 6.6 L11 2.6" fill="none" stroke="var(--silver)" stroke-width="1.2"/></svg>
        info@halspuntmirbe.be
      </li>
      <li>
        <svg viewBox="0 0 12 12" aria-hidden="true"><circle cx="6" cy="6" r="5" fill="none" stroke="var(--silver)" stroke-width="1.1"/><ellipse cx="6" cy="6" rx="2.2" ry="5" fill="none" stroke="var(--silver)" stroke-width="1"/><path d="M1 6 H11" stroke="var(--silver)" stroke-width="1"/></svg>
        www.halspuntmirbe.be
      </li>
    </ul>
    <div class="clinic">
      <div class="clinic-name">HALSPUNT MIRBE</div>
      <div class="clinic-address">Kerkstraat 41</div>
    </div>
  </section>
</main>
</body>
</html>
```